Business Card Re-design

We are looking for a fresh bold look for general office business cards. We are a staffing agency that staffs industrial, coal mining, and clerical jobs.
Tag Line: We connect the RIGHT people with the RIGHT jobs.
Evansville Office: 2473 W. Tallow Creek Rd, Evansville, IN - 47308
p. 555.203.6180 f. 555.203.6195
Princeton Office: 264 S. Birch Ln, Princeton, IN - 47152
p. 555.319.2047 f. 555.203.6195
Absentee/Emergency 24hr Hotline 555.203.6172 opt.1
www.bluelanternworkforce.example

```html
<!DOCTYPE html>
<html lang="en">
<head>
<meta charset="utf-8">
<title>Blue Lantern Workforce – Business Cards</title>
<link rel="stylesheet" href="https://fonts.googleapis.com/css2?family=Source+Sans+3:wght@400;600;700&display=swap">
<style>
  :root {
    --backdrop: #e9e6e1;
    --card-white: #ffffff;
    --card-black: #111213;
    --navy: #1f3e66;
    --blue: #3f6fb0;
    --sky: #7cb8de;
    --green: #3f9c3c;
    --green-bright: #5bbf44;
    --ink: #1b1b1b;
  }
  * { box-sizing: border-box; margin: 0; padding: 0; }
  html, body { width: 1200px; height: 942px; overflow: hidden; }
  body {
    background: var(--backdrop);
    font-family: "Source Sans 3", "Myriad Pro", Arial, sans-serif;
    position: relative;
  }
  .card {
    position: absolute;
    left: 220px;
    width: 760px;
    height: 434px;
    box-shadow: 0 8px 22px rgba(0,0,0,0.25);
    overflow: hidden;
  }
  .card--front { top: 24px; background: var(--card-white); }
  .card--back { top: 484px; background: var(--card-black); }

  /* front */
  .office { position: absolute; color: var(--ink); font-size: 19px; line-height: 1.35; }
  .office__title { font-size: 20px; margin-bottom: 6px; }
  .office--evansville { left: 40px; top: 34px; }
  .office--evansville .office__title { color: var(--blue); }
  .office--princeton { right: 40px; top: 212px; text-align: right; }
  .office--princeton .office__title { color: var(--green); }
  .line { display: flex; align-items: center; gap: 8px; }
  .office--princeton .line { justify-content: flex-end; }
  .phones { display: flex; gap: 26px; margin-top: 4px; }
  .office--princeton .phones { justify-content: flex-end; }
  .icon { width: 18px; height: 18px; flex: none; }
  .icon--blue { fill: var(--blue); }
  .icon--green { fill: var(--green); }

  .brand {
    position: absolute;
    left: 380px; top: 78px;
    width: 340px;
    text-align: center;
  }
  .brand__name {
    color: var(--navy);
    font-weight: 700;
    font-size: 40px;
    line-height: 1.0;
    letter-spacing: 1px;
    text-transform: uppercase;
  }
  .brand__web { color: var(--navy); font-size: 18px; margin-top: 14px; }

  .hotline-band {
    position: absolute;
    left: 0; right: 0; bottom: 0;
    height: 62px;
    background: linear-gradient(90deg, var(--navy) 0%, #6aa7cf 45%, var(--green-bright) 75%, var(--green) 100%);
    color: #fff;
    font-size: 21px;
    display: flex; align-items: center;
    padding-left: 40px;
  }

  /* back */
  .back__content {
    position: absolute; inset: 0;
    display: flex; flex-direction: column; align-items: center; justify-content: center;
    gap: 22px;
  }
  .back__name {
    color: var(--blue);
    font-weight: 700;
    font-size: 52px;
    letter-spacing: 2px;
    text-transform: uppercase;
    line-height: 1;
  }
  .back__tagline { color: #fff; font-size: 22px; }
</style>
</head>
<body>

<section class="card card--front" aria-label="Business card front">
  <div class="office office--evansville">
    <p class="office__title">Evansville Office:</p>
    <p class="line">
      <svg class="icon icon--blue" viewBox="0 0 24 24" aria-hidden="true"><path d="M12 2a7 7 0 0 0-7 7c0 5 7 13 7 13s7-8 7-13a7 7 0 0 0-7-7zm0 9.5A2.5 2.5 0 1 1 12 6.5a2.5 2.5 0 0 1 0 5z"/></svg>
      2473 W. Tallow Creek Rd
    </p>
    <p class="line">Evansville, IN - 47308</p>
    <div class="phones">
      <p class="line">
        <svg class="icon icon--blue" viewBox="0 0 24 24" aria-hidden="true"><path d="M6.6 10.8a15 15 0 0 0 6.6 6.6l2.2-2.2a1 1 0 0 1 1-.25 11 11 0 0 0 3.6.6 1 1 0 0 1 1 1V20a1 1 0 0 1-1 1A17 17 0 0 1 3 4a1 1 0 0 1 1-1h3.5a1 1 0 0 1 1 1c0 1.25.2 2.45.6 3.6a1 1 0 0 1-.25 1z"/></svg>
        555.203.6180
      </p>
      <p class="line">
        <svg class="icon icon--blue" viewBox="0 0 24 24" aria-hidden="true"><path d="M6 2h9v5H6zM4 8h16a2 2 0 0 1 2 2v9a2 2 0 0 1-2 2H4a2 2 0 0 1-2-2v-9a2 2 0 0 1 2-2zm3 4v2h6v-2zm0 4v2h6v-2zm9-3a1.5 1.5 0 1 0 0 .01z"/></svg>
        555.203.6195
      </p>
    </div>
  </div>

  <div class="brand">
    <p class="brand__name">Blue Lantern<br>Workforce</p>
    <p class="brand__web">www.bluelanternworkforce.example</p>
  </div>

  <div class="office office--princeton">
    <p class="office__title">Princeton Office:</p>
    <p class="line">
      264 S. Birch Ln,
      <svg class="icon icon--green" viewBox="0 0 24 24" aria-hidden="true"><path d="M12 2a7 7 0 0 0-7 7c0 5 7 13 7 13s7-8 7-13a7 7 0 0 0-7-7zm0 9.5A2.5 2.5 0 1 1 12 6.5a2.5 2.5 0 0 1 0 5z"/></svg>
    </p>
    <p class="line">Princeton, IN - 47152</p>
    <div class="phones">
      <p class="line">
        555.319.2047
        <svg class="icon icon--green" viewBox="0 0 24 24" aria-hidden="true"><path d="M6.6 10.8a15 15 0 0 0 6.6 6.6l2.2-2.2a1 1 0 0 1 1-.25 11 11 0 0 0 3.6.6 1 1 0 0 1 1 1V20a1 1 0 0 1-1 1A17 17 0 0 1 3 4a1 1 0 0 1 1-1h3.5a1 1 0 0 1 1 1c0 1.25.2 2.45.6 3.6a1 1 0 0 1-.25 1z"/></svg>
      </p>
      <p class="line">
        555.203.6195
        <svg class="icon icon--green" viewBox="0 0 24 24" aria-hidden="true"><path d="M6 2h9v5H6zM4 8h16a2 2 0 0 1 2 2v9a2 2 0 0 1-2 2H4a2 2 0 0 1-2-2v-9a2 2 0 0 1 2-2zm3 4v2h6v-2zm0 4v2h6v-2zm9-3a1.5 1.5 0 1 0 0 .01z"/></svg>
      </p>
    </div>
  </div>

  <div class="hotline-band">Absentee/Emergency 24hr Hotline 555.203.6172 opt.1</div>
</section>

<section class="card card--back" aria-label="Business card back">
  <div class="back__content">
    <p class="back__name">Blue Lantern Workforce</p>
    <p class="back__tagline">We connect the RIGHT people with the RIGHT jobs.</p>
  </div>
</section>

</body>
</html>
```